Unique Extrior cleaning Logo

We need a new business card design, i would like to use our existing logo (attached).
Our logo on the left & a unique graphic design on the right of either a man holding a pressure washer gun & hose with a thumbs up or an image portraying dirt melting off a building or the two incorperated together, or something similar that represents exterior cleaning in progress, an image that shows/explains that we are exterior cleaners/pressure washers. Has to incorporate the quorvix & plinkaroo symbol perhaps in the bottom corners of the business card.
Existing business symbol on the back of the card with some blank lines for space to hand write quotes or job notes.
Industry/Entity Type
Exterior Cleaning
Contact Information for Business Card
Business mobile No. to be prominent (0472 918 306) Services provided listed as dot points. -Soft Washing -Pressure Washing - Solar Panel Cleaning - All General Exterior Cleaning. Email listed in fineprint (enquiries@brindlecrestwashworks.com.au). Owner Operator - Declan Hartley (this should also be added somewhere prominent). Residential & Comercial Cleaning.
Colors
Designer to choose colors to be used in the design.
Look and feel

```html
<!DOCTYPE html>
<html lang="en">
<head>
<meta charset="utf-8">
<title>Brindlecrest Washworks – Business Card</title>
<link href="https://fonts.googleapis.com/css2?family=Roboto:wght@400;700&display=swap" rel="stylesheet">
<style>
  :root {
    --backdrop: #3b3b3d;
    --card: #151516;
    --card-edge: #4a63b8;
    --accent: #4d68c2;
    --ink: #e9e9ea;
    --ink-soft: #bdbdc0;
    --emboss: #2a2a2c;
  }
  * { box-sizing: border-box; margin: 0; padding: 0; }
  html, body {
    width: 1200px; height: 801px; overflow: hidden;
    background: var(--backdrop);
    font-family: "Roboto", Arial, sans-serif;
  }
  .sheet {
    width: 1200px; height: 801px;
    display: flex; align-items: center; justify-content: center; gap: 40px;
  }
  .card {
    position: relative;
    width: 540px; height: 310px;
    background: var(--card);
    border: 1.5px solid var(--card-edge);
    border-radius: 18px;
    box-shadow: 0 18px 40px rgba(0,0,0,.35);
    overflow: hidden;
  }
  /* front */
  .brand {
    position: absolute; left: 34px; top: 70px; width: 200px;
    display: flex; flex-direction: column; align-items: flex-start; gap: 14px;
  }
  .brand-square { width: 40px; height: 40px; background: var(--accent); }
  .brand-name {
    color: var(--ink); font-weight: 700; font-size: 21px;
    letter-spacing: 2px; text-transform: uppercase; line-height: 1.2;
  }
  .divider {
    position: absolute; left: 250px; top: 30px; width: 1px; height: 176px;
    background: var(--accent);
  }
  .divider-foot {
    position: absolute; left: 250px; top: 206px; width: 254px; height: 1px;
    background: var(--accent); opacity: .0;
  }
  .contact {
    position: absolute; left: 272px; top: 36px; right: 20px;
    color: var(--ink); font-size: 12px; line-height: 1.55;
  }
  .contact-name {
    color: var(--accent); font-weight: 700; font-size: 24px;
    text-transform: uppercase; line-height: 1.1;
  }
  .contact-role { font-size: 13px; margin-bottom: 10px; }
  .contact-row { display: flex; align-items: center; gap: 6px; white-space: nowrap; }
  .contact-row svg { width: 11px; height: 11px; flex: none; fill: var(--accent); }
  .contact-phone { color: var(--accent); font-weight: 700; font-size: 15px; }
  .contact-email { font-size: 10.5px; }
  .contact-sector { margin-top: 10px; font-size: 12.5px; }
  .services {
    position: absolute; left: 28px; right: 20px; bottom: 24px;
    color: var(--ink); font-size: 12.5px; white-space: nowrap;
  }
  .services .dot { color: var(--accent); font-weight: 700; margin: 0 4px; }
  /* back */
  .back-brand {
    position: absolute; inset: 0;
    display: flex; flex-direction: column; align-items: center; justify-content: center; gap: 18px;
  }
  .back-square { width: 70px; height: 70px; background: var(--emboss); }
  .back-name {
    color: var(--ink-soft); font-weight: 700; font-size: 28px;
    letter-spacing: 3px; text-transform: uppercase;
  }
</style>
</head>
<body>
<main class="sheet">
  <section class="card card-front">
    <div class="brand">
      <span class="brand-square"></span>
      <span class="brand-name">Brindlecrest<br>Washworks</span>
    </div>
    <span class="divider"></span>
    <div class="contact">
      <p class="contact-name">Declan Hartley</p>
      <p class="contact-role">Owner Operator</p>
      <p class="contact-row contact-phone">
        <svg viewBox="0 0 24 24"><path d="M6.6 10.8a15.1 15.1 0 0 0 6.6 6.6l2.2-2.2a1 1 0 0 1 1-.25 11.4 11.4 0 0 0 3.6.57 1 1 0 0 1 1 1V20a1 1 0 0 1-1 1A17 17 0 0 1 3 4a1 1 0 0 1 1-1h3.5a1 1 0 0 1 1 1c0 1.25.2 2.46.57 3.6a1 1 0 0 1-.25 1z"/></svg>
        0472 918 306
      </p>
      <p class="contact-row contact-email">
        <svg viewBox="0 0 24 24"><path d="M2 5h20v14H2zM4 7v.5l8 5 8-5V7l-8 5z"/></svg>
        enquiries@brindlecrestwashworks.com.au
      </p>
      <p class="contact-row contact-web">
        <svg viewBox="0 0 24 24"><circle cx="12" cy="12" r="10"/></svg>
        www.brindlecrestwashworks.com.au
      </p>
      <p class="contact-sector">Residential &amp; Comercial Cleaning</p>
    </div>
    <p class="services">Soft Washing<span class="dot">•</span>Pressure Washing<span class="dot">•</span>Solar Panel Cleaning<span class="dot">•</span>All General Exterior Cleaning</p>
  </section>

  <section class="card card-back">
    <div class="back-brand">
      <span class="back-square"></span>
      <span class="back-name">Brindlecrest Washworks</span>
    </div>
  </section>
</main>
</body>
</html>
```